Re-design of veterinary clinic website *

For a future relaunch of our webpage, we would like to find a fresh design that still incorporates the spirit of our current one which can be found at http://dr-wenzlaff.de
We are a small business that appeals to locals but are known in a wide area for specialist services.
According to analytics data, most people rarely read through the full website but are using it to inform themselves about opening hours, Telephone numbers and location. Still, the website needs to offer enough content to be ranked positively by the Quandle algorithm.
Our logo is not part of the re-design but needs to be included in your proposal as is. It can be used a source of inspiration, just as the current design. Keep in mind, that the design will be used as the basis of a fluid webdesign for both mobile and desktop. Roughly 75% of our users are on mobile devices.
Target Market(s)
Locals
Industry/Entity Type
Veterinary
Number of Pages Required
1 page
Look and feel
Each slider illustrates characteristics of the customer's brand and the style your logo design should communicate.

```html
<!DOCTYPE html>
<html lang="de">
<head>
<meta charset="utf-8">
<title>Tierarztpraxis Dr. Henrik Wenzlaff</title>
<link href="https://fonts.googleapis.com/css2?family=Mulish:wght@400;600;700;800&display=swap" rel="stylesheet">
<style>
:root{
  --navy:#2b3f8f;
  --sky:#86c9e8;
  --bright:#43aee6;
  --panel-1:#42b3e5;
  --panel-2:#0783cf;
  --panel-3:#2e51a2;
  --ink:#222a33;
  --grey:#444;
  --white:#fff;
}
*{margin:0;padding:0;box-sizing:border-box}
html,body{width:1200px;height:1000px;overflow:hidden;background:var(--white);font-family:'Mulish',sans-serif}
.page{position:relative;width:1200px;height:1000px;overflow:hidden}

.site-header{position:absolute;top:0;left:0;width:1200px;height:88px}
.brand{position:absolute;left:64px;top:14px;display:flex;align-items:center;gap:10px}
.brand-mark{width:26px;height:26px;border:2px solid var(--navy);border-radius:50%}
.brand-name{color:var(--navy);font-weight:700;font-size:19px;letter-spacing:1px;line-height:1.15}
.brand-name small{display:block;font-size:12px;letter-spacing:.5px}
.contact-block{position:absolute;top:6px;display:flex;gap:14px}
.contact-block svg{flex:none;margin-top:6px}
.contact-block h4{color:var(--navy);font-size:14px;font-weight:700;margin-bottom:3px}
.contact-block p{color:var(--grey);font-size:14px;line-height:18px}
.contact-locate{left:646px}
.contact-connect{left:913px;top:8px}

.main-nav{position:absolute;top:88px;left:0;width:1200px;height:45px;background:var(--sky);display:flex}
.main-nav a{display:flex;align-items:center;justify-content:center;color:var(--white);font-weight:700;font-size:19px;text-decoration:none;height:45px}
.main-nav a.current{color:var(--navy)}
.main-nav a.highlight{background:var(--navy)}

.hero{position:absolute;top:133px;left:0;width:1200px;height:454px;
  background:linear-gradient(90deg,#5a9fd0 0%,#7fb8e0 25%,#d9e3ea 45%,#eef1f3 60%,#dfe4e8 75%,#c8ccd1 100%)}
.hero-caption{position:absolute;left:64px;top:142px;width:683px;height:157px;background:rgba(150,205,235,.72);padding:28px 26px}
.hero-caption h1{color:var(--ink);font-size:41px;font-weight:600;line-height:52px}
.hero-caption p{color:var(--navy);font-size:20px;margin-top:4px}

.welcome{position:absolute;top:626px;left:0;width:1200px;text-align:center}
.welcome svg{display:block;margin:0 auto}
.welcome h2{color:var(--navy);font-size:29px;font-weight:700;margin-top:20px}
.welcome p{color:var(--bright);font-size:19px;line-height:24px;margin-top:20px}
.welcome strong{font-weight:700}

.info-panels{position:absolute;top:875px;left:0;width:1200px;height:125px;display:flex;color:var(--white)}
.info-panel{height:125px;padding:28px 26px}
.info-panel h3{font-size:22px;font-weight:400;margin-bottom:14px}
.info-panel p{font-size:14.5px;line-height:19px}
.panel-team{width:399px;background:var(--panel-1)}
.panel-booking{width:401px;background:var(--panel-2)}
.panel-booking p{line-height:24px;margin-top:-2px}
.panel-hours{width:400px;background:var(--panel-3);position:relative;padding:28px 28px}
.panel-hours h3{font-weight:600}
.slider-arrows{position:absolute;right:28px;top:22px;display:flex}
.slider-arrows span{width:34px;height:34px;border:1px solid rgba(255,255,255,.35);display:flex;align-items:center;justify-content:center}
.hours-row{display:flex;justify-content:space-between;font-size:14.5px;font-weight:600;padding-bottom:13px;border-bottom:1px solid rgba(255,255,255,.3)}
</style>
</head>
<body>
<div class="page">
  <header class="site-header">
    <div class="brand">
      <div class="brand-mark"></div>
      <div class="brand-name"><small>Dr. med. vet.</small>Henrik Wenzlaff</div>
    </div>
    <div class="contact-block contact-locate">
      <svg width="28" height="40" viewBox="0 0 28 40" fill="none" stroke="#86c9e8" stroke-width="1.6"><path d="M14 38C14 38 2 22 2 14a12 12 0 0 1 24 0c0 8-12 24-12 24z"/><circle cx="14" cy="14" r="4.5"/></svg>
      <div><h4>Locate us</h4><p>Lindenweg 14b<br>14163 Berlin (Zehlendorf)</p></div>
    </div>
    <div class="contact-block contact-connect">
      <svg width="38" height="34" viewBox="0 0 38 34" fill="none" stroke="#86c9e8" stroke-width="1.6"><path d="M2 2h34v22H14l-8 7v-7H2z"/><path d="M9 9h20M9 14h20M9 19h14"/></svg>
      <div><h4>Connect us</h4><p>Telefon: 030 / 555 21 40<br>Telefax: 030 / 555 21 49</p></div>
    </div>
  </header>

  <nav class="main-nav">
    <a class="current" href="#" style="width:252px">Hauptseite</a>
    <a href="#" style="width:76px">Praxis</a>
    <a href="#" style="width:225px">Team</a>
    <a href="#" style="width:133px">Sprechzeiten</a>
    <a href="#" style="width:244px">Leistungen</a>
    <a class="highlight" href="#" style="width:217px;margin-left:-16px">Kontakt und Anfahrt</a>
  </nav>

  <section class="hero" role="img" aria-label="Tierärztin in blauer Kleidung untersucht einen Hund auf dem Behandlungstisch">
    <div class="hero-caption">
      <h1>Experienced Veterinarians</h1>
      <p>Your pet is in good hands, meet our highly qualified professionals</p>
    </div>
  </section>

  <section class="welcome">
    <svg width="42" height="38" viewBox="0 0 42 38" fill="#6ab8e6"><ellipse cx="7" cy="16" rx="5" ry="6"/><ellipse cx="15" cy="6" rx="5" ry="6"/><ellipse cx="27" cy="6" rx="5" ry="6"/><ellipse cx="35" cy="16" rx="5" ry="6"/><path d="M21 17c-6 0-13 10-13 15 0 5 6 5 13 3 7 2 13 2 13-3 0-5-7-15-13-15z"/></svg>
    <h2>Herzlich Willkommen!</h2>
    <p>Herzlich Willkommen auf der Homepage der Tierarztpraxis von <strong>Dr. Henrik Wenzlaff</strong>.<br>Mein Team und ich haben hier Informationen rund um die Praxis und<br>Hinweise für Patientenbesitzer zusammengestellt.</p>
  </section>

  <section class="info-panels">
    <div class="info-panel panel-team">
      <h3>Meet Our Team</h3>
      <p>Das Praxisteam besteht aus einer angestellten Tierärztin, einem angestellten Tierarzt, mehreren tiermedizinischen</p>
    </div>
    <div class="info-panel panel-booking">
      <h3>Book Appointment</h3>
      <p>We will review your request<br>and confirm your appointment</p>
    </div>
    <div class="info-panel panel-hours">
      <h3>Opening Hours</h3>
      <div class="slider-arrows">
        <span><svg width="8" height="12" viewBox="0 0 8 12" fill="none" stroke="#fff" stroke-width="1.5"><path d="M6 1L1 6l5 5"/></svg></span>
        <span><svg width="8" height="12" viewBox="0 0 8 12" fill="none" stroke="#fff" stroke-width="1.5"><path d="M2 1l5 5-5 5"/></svg></span>
      </div>
      <div class="hours-row"><span>Monday - Thursday</span><span>8.00 - 17.00</span></div>
    </div>
  </section>
</div>
</body>
</html>
```